Non-governmental organisation branding design

We are looking to get the branding for our new NGO:

Kestrel Harbour Centre

Our tag-line is: Peace through dialogue

We are a peace brokering organisation that conducts research and offers peace brokering services relating to conflicts around the world.

The branding needs to be simple, to the point and serious.

Other comparable organisations are:

https://www.vantrellhub.org/

http://tlx.fi/

https://www.oravelle.org/

Any questions, please get in touch.

Logo Text

Kestrel Harbour Centre

Number of Pages Required

1 page

```html
<!DOCTYPE html>
<html lang="en">
<head>
<meta charset="utf-8">
<title>Kestrel Harbour Centre — Peace Through Dialogue</title>
<link rel="stylesheet" href="https://fonts.googleapis.com/css2?family=Lato:wght@400;700&family=Open+Sans:wght@400;600&family=Roboto:wght@400;500&display=swap">
<style>
:root{
  --blue:#3e8ed0;
  --blue-bright:#4aa3e0;
  --blue-dark:#1f6fb8;
  --ink:#1b1b1b;
  --text:#555;
  --nav-active:#111;
  --gray:#e8e8e8;
  --footer:#13222e;
  --footer-text:#d8dee3;
  --navy-btn:#1c2d3a;
  --white:#fff;
}
*{box-sizing:border-box;margin:0;padding:0}
html,body{width:1200px;height:2857px;overflow:hidden;background:var(--white)}
body{font-family:"Open Sans",sans-serif;color:var(--ink);position:relative}

.site-nav{height:46px;background:var(--blue);display:flex;justify-content:center}
.site-nav ul{display:flex;list-style:none;margin-left:-30px}
.site-nav li{font-family:"Lato",sans-serif;font-size:14px;color:var(--white);line-height:46px;padding:0 21px;letter-spacing:.2px}
.site-nav li.active{background:var(--nav-active);padding:0 26px}

.hero{position:relative;height:669px;overflow:hidden}
.hero-photo{position:absolute;inset:0;background:radial-gradient(ellipse at 45% 40%,#5a5d62 0%,#3b3e43 45%,#24272b 100%)}
.hero-content{position:relative;text-align:center;color:var(--white)}
.brand-mark{width:62px;height:62px;border:4px solid var(--white);border-radius:50%;margin:110px auto 0}
.brand-name{font-family:"Lato",sans-serif;font-size:37px;line-height:40px;margin-top:10px;font-weight:400;letter-spacing:.5px;color:var(--white)}
.hero-tagline{font-family:"Lato",sans-serif;font-weight:700;font-size:43px;margin-top:42px;letter-spacing:.5px}
.scroll-down{width:46px;height:46px;border:2px solid var(--white);border-radius:50%;margin:48px auto 0;display:flex;align-items:center;justify-content:center}
.hero-curve{position:absolute;left:0;bottom:0;width:1200px;height:180px}

.what-we-do{height:237px;text-align:center}
.faint-mark{width:46px;height:46px;border-radius:50%;background:#cfcfcf;margin:-46px auto 0;position:relative}
.section-title{font-family:"Lato",sans-serif;font-weight:400;font-size:28px;color:var(--ink);letter-spacing:.3px}
.what-we-do .section-title{margin-top:8px}
.title-rule{width:46px;height:3px;background:var(--blue);margin:10px auto 0}
.intro{width:700px;margin:22px auto 0;font-size:17.5px;line-height:29px;color:var(--text)}
.btn-outline{display:inline-block;border:2px solid var(--ink);color:var(--blue-dark);font-family:"Lato",sans-serif;font-size:15px;padding:0;width:148px;height:40px;line-height:36px;margin-top:30px}

.services{position:relative;background:var(--gray);height:570px}
.services-curve{position:absolute;top:0;left:0;width:1200px;height:120px}
.services .section-title{position:absolute;top:164px;left:0;right:0;text-align:center;font-size:25px}
.services .title-rule{position:absolute;top:196px;left:577px;margin:0}
.card-row{position:absolute;top:282px;left:185px;display:flex;gap:14px}
.service-card{position:relative;width:268px;height:176px;background:var(--white);border-top:4px solid var(--blue);box-shadow:0 0 0 1px #d4d4d4;text-align:center}
.service-icon{position:absolute;top:-48px;left:88px;width:92px;height:92px;border-radius:50%;background:var(--blue-dark);border:4px solid #dfe9f3;display:flex;align-items:center;justify-content:center}
.service-card h3{font-family:"Roboto",sans-serif;font-weight:500;font-size:19px;margin-top:54px;color:#111}
.service-card p{font-size:11px;line-height:15px;color:#666;width:225px;margin:10px auto 0}
.btn-pill{position:absolute;bottom:-15px;left:72px;width:124px;height:30px;border-radius:15px;background:var(--navy-btn);color:var(--white);font-family:"Roboto",sans-serif;font-size:14px;line-height:30px}

.news{height:579px;position:relative}
.news .section-title{position:absolute;left:185px;top:44px;font-size:25px}
.news .title-rule{position:absolute;left:185px;top:82px;margin:0}
.news-item{position:absolute;overflow:hidden;color:var(--white)}
.news-item .photo{position:absolute;inset:0}
.news-caption{position:absolute;left:25px;right:20px;bottom:18px}
.news-date{font-family:"Roboto",sans-serif;font-weight:500;font-size:11px}
.news-title{color:var(--blue-bright);font-size:17px;margin-top:6px}
.news-excerpt{font-size:11px;margin-top:4px}
.news-small .news-title{font-size:15px;margin-top:3px}
.news-small .news-caption{bottom:14px}

.banner{position:relative;height:370px;text-align:center;color:var(--white)}
.banner .photo{position:absolute;inset:0;background:linear-gradient(135deg,#5a8fbd 0%,#3f79b0 45%,#6a9cc8 100%)}
.banner-text{position:relative;padding-top:118px;font-family:"Lato",sans-serif}
.banner-text h2{font-weight:400;font-size:31px;letter-spacing:.4px}
.banner-text p{font-size:24px;margin-top:2px;letter-spacing:.4px}
.btn-ghost{display:inline-block;width:146px;height:38px;border:2px solid var(--white);line-height:34px;font-size:14px;margin-top:24px}

.site-footer{position:relative;height:386px;background:var(--footer);color:var(--footer-text)}
.footer-brand{position:absolute;left:205px;top:72px;width:200px;text-align:center}
.footer-brand .brand-mark{width:44px;height:44px;border-width:3px;margin:0 auto}
.footer-brand .brand-name{font-size:25px;line-height:28px;margin-top:10px}
.footer-col{position:absolute;top:72px}
.footer-col h4{font-family:"Lato",sans-serif;font-weight:400;font-size:17px;color:var(--white);margin-bottom:12px}
.footer-col li{list-style:none;font-size:12px;line-height:22.5px}
.socials{display:flex;gap:5px;margin-top:12px}
.socials span{width:29px;height:29px;border-radius:50%;background:var(--white)}
.footer-rule{position:absolute;left:206px;width:800px;height:1px;background:#33434f}
.newsletter{position:absolute;left:229px;top:282px;display:flex;align-items:center}
.newsletter label{font-family:"Lato",sans-serif;font-size:16px;color:var(--blue-bright);width:190px;letter-spacing:.5px}
.newsletter .field{width:430px;height:34px;border-radius:17px 0 0 17px;background:#2c3b47;color:#9aa6af;font-size:12px;line-height:34px;padding-left:18px}
.newsletter .subscribe{width:124px;height:34px;border-radius:17px;background:var(--blue);color:var(--white);font-family:"Lato",sans-serif;font-size:14px;line-height:34px;text-align:center;margin-left:-20px}
.copyright{position:absolute;top:350px;left:0;right:0;text-align:center;font-size:12px;color:#8794a0}
</style>
</head>
<body>

<nav class="site-nav">
  <ul>
    <li class="active">HOME</li><li>ABOUT US</li><li>WHY US</li><li>NEWS &amp; PRESS</li><li>BLOGS</li><li>RESOURCES</li><li>CONTACT US</li>
  </ul>
</nav>

<header class="hero">
  <div class="hero-photo" role="img" aria-label="Photo of people in a mediation session, darkened"></div>
  <div class="hero-content">
    <div class="brand-mark"></div>
    <div class="brand-name">KESTREL HARBOUR CENTRE</div>
    <h1 class="hero-tagline">PEACE THROUGH DIALOGUE</h1>
    <div class="scroll-down">
      <svg width="18" height="12" viewBox="0 0 18 12"><path d="M2 2l7 7 7-7" fill="none" stroke="#fff" stroke-width="3"/></svg>
    </div>
  </div>
  <svg class="hero-curve" viewBox="0 0 1200 180" preserveAspectRatio="none"><path d="M0 180 Q600 8 1200 180 Z" fill="#fff"/></svg>
</header>

<section class="what-we-do">
  <div class="faint-mark"></div>
  <h2 class="section-title">WHAT WE DO</h2>
  <div class="title-rule"></div>
  <p class="intro">Morbi eget arcu Morbi porta libero id ullamcorper nonummy nibh ligula pulvinar metus eget consectetuer augue nisi quis lacus Ut ac mi quis lacus mollis aliquam vvscelerisque mi tortor at ipsum cligula augue bibendum accumsan vestibulum ut</p>
  <span class="btn-outline">READ MORE</span>
</section>

<section class="services">
  <svg class="services-curve" viewBox="0 0 1200 120"><path d="M0 0 H1200 Q600 192 0 0 Z" fill="#fff"/><path d="M110 28 Q600 164 1090 28" fill="none" stroke="#3e8ed0" stroke-width="3"/></svg>
  <h2 class="section-title">OUR SERVICES</h2>
  <div class="title-rule"></div>
  <div class="card-row">
    <article class="service-card">
      <div class="service-icon"><svg width="46" height="46" viewBox="0 0 46 46" fill="none" stroke="#fff" stroke-width="2"><circle cx="17" cy="23" r="12"/><circle cx="29" cy="23" r="12"/></svg></div>
      <h3>Conflict Resolution</h3>
      <p>Morbi eget arcu Morbi porta libero id ullamcorper nonummy nibh ligula pulvinar metus eget consectetuer augue</p>
      <span class="btn-pill">Learn More</span>
    </article>
    <article class="service-card">
      <div class="service-icon"><svg width="46" height="46" viewBox="0 0 46 46" fill="none" stroke="#fff" stroke-width="2"><circle cx="23" cy="21" r="15"/><path d="M16 21h14M23 14v14"/></svg></div>
      <h3>Conflict Prevention</h3>
      <p>Morbi eget arcu Morbi porta libero id ullamcorper nonummy nibh ligula pulvinar metus eget consectetuer augue</p>
      <span class="btn-pill">Learn More</span>
    </article>
    <article class="service-card">
      <div class="service-icon"><svg width="46" height="46" viewBox="0 0 46 46" fill="none" stroke="#fff" stroke-width="2"><circle cx="23" cy="14" r="6"/><path d="M10 38 L23 24 L36 38 Z"/></svg></div>
      <h3>Mediation Expertise</h3>
      <p>Morbi eget arcu Morbi porta libero id ullamcorper nonummy nibh ligula pulvinar metus eget consectetuer augue</p>
      <span class="btn-pill">Learn More</span>
    </article>
  </div>
</section>

<section class="news">
  <h2 class="section-title">LATEST NEWS</h2>
  <div class="title-rule"></div>
  <article class="news-item" style="left:185px;top:107px;width:505px;height:390px">
    <div class="photo" role="img" aria-label="Photo of a counselling conversation between three adults" style="background:linear-gradient(180deg,#a9b3bb 0%,#6b737a 55%,#2a2d31 100%)"></div>
    <div class="news-caption">
      <div class="news-date">25 JUNE 2018</div>
      <div class="news-title">Aorquent per conubia nostra per inceptos hymenaeos</div>
      <div class="news-excerpt">Proin nulla arcu nonummy luctus dictum eget fermentum ut lorem</div>
    </div>
  </article>
  <article class="news-item news-small" style="left:699px;top:107px;width:322px;height:192px">
    <div class="photo" role="img" aria-label="Photo of a group seated in a discussion circle" style="background:linear-gradient(180deg,#7d7a74 0%,#4e4c49 60%,#27282a 100%)"></div>
    <div class="news-caption">
      <div class="news-date">18 JUNE 2018</div>
      <div class="news-title">Aliquam erat volutpat</div>
      <div class="news-excerpt">Proin nulla arcu nonummy luctus dictum eget</div>
    </div>
  </article>
  <article class="news-item news-small" style="left:699px;top:307px;width:322px;height:190px">
    <div class="photo" role="img" aria-label="Photo of two colleagues talking in an office" style="background:linear-gradient(180deg,#8f969c 0%,#5b6167 60%,#26292c 100%)"></div>
    <div class="news-caption">
      <div class="news-date">18 JUNE 2018</div>
      <div class="news-title">Mauris vel lacus vitae felt</div>
      <div class="news-excerpt">Proin nulla arcu nonummy luctus dictum eget</div>
    </div>
  </article>
</section>

<section class="banner">
  <div class="photo" role="img" aria-label="Blue-tinted photo of people in a group discussion"></div>
  <div class="banner-text">
    <h2>TORQUENT PER CONUBIA NOSTRA PER INCEPTOS</h2>
    <p>HYMENAEOS PROIN NULLA ARCU NONUMMY</p>
    <span class="btn-ghost">READ MORE</span>
  </div>
</section>

<footer class="site-footer">
  <div class="footer-brand">
    <div class="brand-mark"></div>
    <div class="brand-name">KESTREL HARBOUR CENTRE</div>
  </div>
  <div class="footer-col" style="left:490px">
    <h4>QUICK LINKS</h4>
    <ul><li>Home</li><li>About Us</li><li>Our Mission</li><li>What We Do</li><li>Blogs</li></ul>
  </div>
  <div class="footer-col" style="left:678px">
    <h4>RESOURCES</h4>
    <ul><li>News</li><li>Media</li><li>Our Projects</li><li>Support</li><li>Contact Us</li></ul>
  </div>
  <div class="footer-col" style="left:850px;top:70px">
    <h4>CONTACT US</h4>
    <ul><li>48 Marrow Lane #4B</li><li>Ashford 20417 AF</li><li>555.014.3826</li><li>hello@kestrelharbour.org</li></ul>
    <div class="socials"><span></span><span></span><span></span><span></span></div>
  </div>
  <div class="footer-rule" style="top:263px"></div>
  <div class="newsletter">
    <label>NEWSLETTER SIGN UP</label>
    <div class="field">Email address</div>
    <div class="subscribe">SUBSCRIBE</div>
  </div>
  <div class="footer-rule" style="top:326px"></div>
  <div class="copyright">© 2018 Kestrel Harbour Centre. All right reserved</div>
</footer>

</body>
</html>
```